Mobile Recording Studio needs business cards

Open to seeing a creative design, but I want to emphasis my logo and minimize the name/title and company information. Possible a fully black background on card.

My company is a mobile sound recording studio. ok to include a my trailer (actual or cartoon) on the card. My initial thought is more straight forward, but a good design will win me over.

SPECS:
CMYK color mode
High (300ppi) raster effect.
cover bleed area
please deliver: Illustrator file with layers and a pdf at completion.

Name and info for the business card:

Dallin Perry
ADR Mixer

email: Dallin@MixVault.com

address:
248 - 5170 East Hollister
Vancouver, BC V5R 2J4

phone:
604.518.2093 office

website:
www.MixVault.com

FB: @MixVault

Instagram: @TheMixVault

Industry/Entity Type

Television Production

Contact Information for Business Card

Dallin Perry
ADR Mixer

email: Dallin@MixVault.com

address:
248 - 5170 East Hollister
Vancouver, BC V5R 2J4

phone:
604.518.2093 office

website:
www.MixVault.com

FB: @MixVault

Instagram: @TheMixVault

Colors

Designer to choose colors to be used in the design.

Requirements
Must have
• emphasis my logo and minimize the name/title and company information.
• SPECS:
• CMYK color mode
• High (300ppi) raster effect.
• cover bleed area
• please deliver: Illustrator file with layers and a pdf at completion.
Nice to have
• maybe include the following:
• all black background or black theme
• my work trailer (actual or cartoon) refer to Instagram: @TheMixVault

```html
<!DOCTYPE html>
<html lang="en">
<head>
<meta charset="utf-8">
<title>The Mix Vault — Business Cards</title>
<link href="https://fonts.googleapis.com/css2?family=Open+Sans:wght@400;600&display=swap" rel="stylesheet">
<style>
  :root {
    --backdrop: #2b2b2b;
    --card-white: #ffffff;
    --charcoal: #3b3b3b;
    --band-grey: #8c8c8c;
    --text-light: #ffffff;
    --logo-silver: #8f8f8f;
    --logo-silver-light: #d9d9d9;
    --sky-top: #8d949b;
    --tree-mid: #5e5a52;
    --grass: #6f8a45;
    --overlay: rgba(30, 30, 30, 0.72);
  }
  * { margin: 0; padding: 0; box-sizing: border-box; }
  html, body {
    width: 1200px; height: 1200px; overflow: hidden;
    background: var(--backdrop);
    font-family: "Open Sans", sans-serif;
  }
  .card {
    position: absolute;
    left: 288px;
    width: 706px;
    height: 402px;
    border-radius: 14px;
    overflow: hidden;
    box-shadow: 0 6px 14px rgba(0,0,0,0.45);
  }
  .card-front { top: 190px; background: var(--card-white); }
  .card-back { top: 662px; }
  .front-shapes { position: absolute; inset: 0; }
  .front-logo {
    position: absolute;
    left: 40px; top: 150px;
    width: 300px;
    text-align: center;
    font-weight: 600;
    font-size: 46px;
    line-height: 1.05;
    color: var(--logo-silver);
    letter-spacing: 1px;
  }
  .identity {
    position: absolute;
    right: 50px; top: 34px;
    text-align: right;
    color: var(--text-light);
  }
  .identity .name { font-size: 24px; font-weight: 400; line-height: 1.2; }
  .identity .title { font-size: 17px; line-height: 1.2; }
  .contact-list {
    position: absolute;
    right: 34px; top: 226px;
    list-style: none;
    color: var(--text-light);
    font-size: 16px;
    line-height: 1.15;
  }
  .contact-list li {
    display: flex; justify-content: flex-end; align-items: flex-start;
    gap: 8px; margin-bottom: 5px; text-align: right;
  }
  .contact-list .icon { width: 13px; height: 13px; flex: none; margin-top: 3px; }
  .scene-photo {
    position: absolute; inset: 0;
    background: linear-gradient(180deg, var(--sky-top) 0%, #6f757b 22%, var(--tree-mid) 55%, #3e3e3c 72%, var(--grass) 86%, #5d7440 100%);
  }
  .logo-band {
    position: absolute;
    left: 0; right: 0; top: 100px; height: 228px;
    background: var(--overlay);
  }
  .back-logo {
    position: absolute;
    left: 0; right: 0; top: 150px;
    text-align: center;
    font-weight: 600;
    font-size: 58px;
    line-height: 1.1;
    color: var(--logo-silver-light);
    letter-spacing: 1px;
  }
</style>
</head>
<body>

<section class="card card-front">
  <svg class="front-shapes" width="706" height="402" viewBox="0 0 706 402">
    <path fill="var(--band-grey)" d="M396,0 L706,0 L706,402 L336,402 C372,320 420,170 396,0 Z"/>
    <path fill="var(--charcoal)" d="M428,0 L706,0 L706,402 L352,402 C390,330 408,300 408,150 L428,150 Z"/>
    <path fill="#a8a8a8" d="M408,150 L428,150 L428,172 Z"/>
  </svg>

  <div class="front-logo">The Mix Vault</div>

  <div class="identity">
    <p class="name">Dallin Perry</p>
    <p class="title">ADR Mixer</p>
  </div>

  <ul class="contact-list">
    <li><span>604.518.2093</span>
      <svg class="icon" viewBox="0 0 14 14"><circle cx="7" cy="7" r="7" fill="#fff"/><path d="M4.3,3.6 L5.7,3.4 L6.4,5.3 L5.6,6 C6.1,7 7,7.9 8,8.4 L8.7,7.6 L10.6,8.3 L10.4,9.7 C7,10 4,7 4.3,3.6 Z" fill="var(--charcoal)"/></svg>
    </li>
    <li><span>FB: @MixVault</span>
      <svg class="icon" viewBox="0 0 14 14"><circle cx="7" cy="7" r="7" fill="#fff"/></svg>
    </li>
    <li><span>www.MixVault.com</span>
      <svg class="icon" viewBox="0 0 14 14"><circle cx="7" cy="7" r="7" fill="#fff"/></svg>
    </li>
    <li><span>Instagram: @TheMixVault</span>
      <svg class="icon" viewBox="0 0 14 14"><circle cx="7" cy="7" r="7" fill="#fff"/></svg>
    </li>
    <li><span>248 - 5170 East Hollister<br>Vancouver, BC V5R 2J4</span>
      <svg class="icon" viewBox="0 0 14 14"><circle cx="7" cy="7" r="7" fill="#fff"/><path d="M7,2.8 C5.3,2.8 4.3,4 4.3,5.4 C4.3,7.3 7,11 7,11 C7,11 9.7,7.3 9.7,5.4 C9.7,4 8.7,2.8 7,2.8 Z" fill="var(--charcoal)"/><circle cx="7" cy="5.4" r="1.1" fill="#fff"/></svg>
    </li>
  </ul>
</section>

<section class="card card-back">
  <div class="scene-photo" role="img" aria-label="Photo of the mobile recording trailer parked beside a path with bare trees under a cloudy sky"></div>
  <div class="logo-band"></div>
  <div class="back-logo">The Mix Vault</div>
</section>

</body>
</html>
```